Online Rug Store needs Clearance Banner

Website is: Lanternfield Carpets and Home
You can access it at: www.lanternfieldcarpetsandhome.com and login (top right) with password: trazok

*** update: When creating banners for my site, you have permission to use images from www.velbora.com, but ONLY for this project. The images/artwork are copyright allowable for use on www.lanternfieldcarpetsandhome.com projects.***

We need a home page banner sized 1000 wide x 500 tall pixels to promote a "Clearance Sale" on rugs. The banner can state:

1. Clearance Sale
2. Now in progress
3. Save an extra 20% with coupon code 'Mint20'
4. Ends March 31st
5. Plus Free Shipping and 30 day returns.

We prefer a banner that appears hand-drawn and artistic, not commercially produced. It is OK to use a room scene image, rug images, or just a colored/textured background with text and no images. Your choice.

Flat graphics with no shadows and 3-D effect preferred.
Attached is are 3 logo options, as well as an example banner with handcrafted, artistic styling that we prefer.

Target Market(s)

This should be an eye-catching banner to showcase a very urgent promotion. Consider using colors of red, white, gold, and black to make a strong statement on the home page.

Industry/Entity Type

Home And Garden

Requirements
Must have
• Winner must provide Photoshop editable file format (.psd format) including layers that can be edited.
Nice to have
• Hand-drawn, stenciled, scribbled, artistic graphics and fonts is nice because we sell rugs that are made by hand.
Should not have
• little to no shadowing. Avoid computerized graphics.

```html
<!DOCTYPE html>
<html lang="en">
<head>
<meta charset="utf-8">
<title>Clearance Sale Banner</title>
<link rel="stylesheet" href="https://fonts.googleapis.com/css2?family=Cinzel:wght@400;700&family=Permanent+Marker&display=swap">
<style>
  :root {
    --band-red: rgba(150, 8, 10, 0.82);
    --ink-white: #ffffff;
    --ink-gold: #ffd21a;
    --rug-1: #7f2a1c;
    --rug-2: #8a8a6a;
    --rug-3: #2f9a8a;
    --rug-4: #c2561c;
    --rug-5: #7d8588;
    --rug-6: #d9598a;
    --rug-7: #3a3433;
    --rug-8: #6f8fa0;
    --rug-9: #cdbd9d;
    --rug-10: #4a3550;
    --rug-11: #c8b552;
  }
  * { margin: 0; padding: 0; box-sizing: border-box; }
  html, body { width: 1200px; height: 600px; overflow: hidden; background: #ffffff; }
  .banner { position: relative; width: 1200px; height: 600px; overflow: hidden; }
  .rug-strips { position: absolute; inset: 0; display: flex; }
  .rug-strip { flex: 1; height: 100%; border-right: 2px solid rgba(255,255,255,0.6); }
  .rug-strip:last-child { border-right: none; }
  .rug-strip--1 { background: linear-gradient(180deg, #6e8a3a 0%, var(--rug-1) 12%, var(--rug-1) 88%, #7a9a48 100%); }
  .rug-strip--2 { background: linear-gradient(180deg, #9a9a7a, var(--rug-2) 50%, #4a4a3a); }
  .rug-strip--3 { background: linear-gradient(180deg, #38a896, var(--rug-3) 50%, #1f7a6c); }
  .rug-strip--4 { background: linear-gradient(180deg, #d46a2a, var(--rug-4) 50%, #9a3e12); }
  .rug-strip--5 { background: linear-gradient(180deg, #8a9296, var(--rug-5) 50%, #5e6669); }
  .rug-strip--6 { background: linear-gradient(180deg, #e36a98, var(--rug-6) 50%, #b8b0c0); }
  .rug-strip--7 { background: linear-gradient(180deg, #2e2a29, var(--rug-7) 50%, #8a8a8e); }
  .rug-strip--8 { background: linear-gradient(180deg, #8aa6b2, var(--rug-8) 50%, #2b4a58); }
  .rug-strip--9 { background: linear-gradient(180deg, #ddd0b4, var(--rug-9) 50%, #b8a47e); }
  .rug-strip--10 { background: linear-gradient(180deg, #3c2a45, var(--rug-10) 50%, #5a4466); }
  .rug-strip--11 { background: linear-gradient(180deg, #d6c670, var(--rug-11) 50%, #b3a042); }

  .sale-band {
    position: absolute; left: 0; right: 0; top: 48px; height: 486px;
    background: var(--band-red);
    text-align: center; color: var(--ink-white);
  }
  .sale-title {
    font-family: "Permanent Marker", cursive;
    font-weight: 400; font-size: 104px; letter-spacing: 8px;
    text-transform: uppercase; line-height: 1;
    margin-top: 92px;
  }
  .sale-status {
    font-family: "Cinzel", serif; font-weight: 400;
    font-size: 42px; letter-spacing: 1px; line-height: 1;
    margin-top: 22px;
  }
  .sale-coupon {
    font-family: "Permanent Marker", cursive;
    font-size: 33px; color: var(--ink-gold); line-height: 1;
    margin-top: 28px; letter-spacing: 0.5px;
  }
  .sale-terms {
    font-family: "Cinzel", serif; font-weight: 700;
    font-size: 27px; line-height: 1;
    margin-top: 42px;
  }
</style>
</head>
<body>
<div class="banner">
  <div class="rug-strips">
    <div class="rug-strip rug-strip--1" role="img" aria-label="Red rug with large floral pattern"></div>
    <div class="rug-strip rug-strip--2" role="img" aria-label="Olive and grey rug with leaf motif"></div>
    <div class="rug-strip rug-strip--3" role="img" aria-label="Teal rug with geometric blocks"></div>
    <div class="rug-strip rug-strip--4" role="img" aria-label="Orange rug with woven pattern"></div>
    <div class="rug-strip rug-strip--5" role="img" aria-label="Grey rug with oval lattice pattern"></div>
    <div class="rug-strip rug-strip--6" role="img" aria-label="Pink striped rug"></div>
    <div class="rug-strip rug-strip--7" role="img" aria-label="Black and pink block rug"></div>
    <div class="rug-strip rug-strip--8" role="img" aria-label="Blue rug with large flower motif"></div>
    <div class="rug-strip rug-strip--9" role="img" aria-label="Beige rug with tribal pattern"></div>
    <div class="rug-strip rug-strip--10" role="img" aria-label="Deep purple shag rug"></div>
    <div class="rug-strip rug-strip--11" role="img" aria-label="Gold rug with trellis pattern"></div>
  </div>

  <div class="sale-band">
    <h1 class="sale-title">Clearance Sale</h1>
    <p class="sale-status">NOW IN PROGRESS</p>
    <p class="sale-coupon">Save an extra 20% with coupon code 'Mint20'</p>
    <p class="sale-terms">Ends March 31st. Free Shipping and 30 day returns.</p>
  </div>
</div>
</body>
</html>
```